HOME IMPROVEMENT Business Card

I want a very unique business card. nothing typical and boring. Im open to you ideas. Ive seen cards with gold and silver or color foil and spot UV coatings. Im looking for something that looks cool and grabs attention. I like rounded corners but am open to all suggestions. We are a home improvement company and I will have a presentation folder printed and a catalog printed also and want to keep that same theme. I love the colors in our logo but I am open at looking at a 3rd color that would work with my logo. I hope that helps.
Card should include
Address
Phone
Fax
Email
Website
Target Market(s)
Home owners, people looking to remodel their home
Industry/Entity Type
Home Improvement
Contact Information for Business Card
2873 Maple Crest Avenue Unit 410
Willow Park, Il 60284
Phone
Direct Line
Email
Website
Font styles to use
Other font styles liked:
- IM OPEN MINDED
Requirements
Must have
- High end quality look nothing boring I like rounded corners but am open minded
Nice to have
- WOW. I want something nice and impressive.
Should not have
- ??? Not sure

```html
<!DOCTYPE html>
<html lang="en">
<head>
<meta charset="utf-8">
<title>Hearthline Remodeling Group – Business Card</title>
<link href="https://fonts.googleapis.com/css2?family=Montserrat:wght@800&family=Roboto:wght@400;700&display=swap" rel="stylesheet">
<style>
  :root {
    --green: #00964a;
    --navy: #141a4a;
    --white: #ffffff;
    --backdrop: #6b7175;
    --ink-light: #ffffff;
  }
  * { box-sizing: border-box; margin: 0; padding: 0; }
  html, body { width: 1200px; height: 900px; overflow: hidden; }
  body {
    background: var(--backdrop);
    display: flex;
    align-items: center;
    justify-content: center;
    gap: 40px;
    font-family: "Roboto", Arial, sans-serif;
  }
  .card {
    position: relative;
    width: 540px;
    height: 309px;
    border-radius: 18px;
    overflow: hidden;
    box-shadow: 0 10px 24px rgba(0,0,0,0.35);
  }
  /* Front */
  .card-front {
    background: var(--green);
    display: flex;
    flex-direction: column;
    align-items: center;
    justify-content: center;
  }
  .brand {
    display: flex;
    align-items: center;
    gap: 12px;
    font-family: "Montserrat", Arial, sans-serif;
    font-weight: 800;
    color: var(--navy);
    line-height: 1.05;
  }
  .brand-mark {
    width: 18px; height: 18px;
    background: var(--navy);
    flex: none;
  }
  .brand-name { font-size: 40px; }
  .brand-sub { font-size: 14px; letter-spacing: 4px; text-transform: uppercase; }
  .card-front .website {
    margin-top: 34px;
    color: var(--navy);
    font-size: 15px;
  }
  /* Back */
  .card-back { background: var(--green); }
  .card-back svg.panel { position: absolute; inset: 0; }
  .contact {
    position: absolute;
    left: 28px; top: 30px;
    color: var(--ink-light);
    font-size: 13px;
    line-height: 1.45;
  }
  .person-name { font-size: 19px; text-transform: uppercase; }
  .person-name strong { font-weight: 700; }
  .person-role { font-size: 12px; text-transform: uppercase; margin-bottom: 12px; }
  .address { margin-bottom: 6px; }
  .contact-row { display: flex; align-items: center; gap: 8px; }
  .contact-row svg { width: 12px; height: 12px; flex: none; }
  .card-back .brand {
    position: absolute;
    right: 30px; top: 118px;
  }
  .card-back .brand-name { font-size: 30px; }
  .card-back .brand-sub { font-size: 11px; letter-spacing: 3px; }
  .card-back .brand-mark { width: 14px; height: 14px; }
</style>
</head>
<body>

  <section class="card card-front">
    <div class="brand">
      <span class="brand-mark"></span>
      <div>
        <div class="brand-name">Hearthline</div>
        <div class="brand-sub">Remodeling Group</div>
      </div>
    </div>
    <p class="website">www.hearthline.com</p>
  </section>

  <section class="card card-back">
    <svg class="panel" viewBox="0 0 540 309" aria-hidden="true">
      <circle cx="520" cy="250" r="250" fill="none" stroke="var(--navy)" stroke-width="6"/>
      <circle cx="526" cy="256" r="240" fill="var(--white)"/>
    </svg>

    <div class="contact">
      <p class="person-name"><strong>Dorian</strong> Kessler</p>
      <p class="person-role">Founder</p>
      <p class="address">2873 Maple Crest Avenue Unit 410<br>Willow Park, Il 60284</p>
      <p class="contact-row">
        <svg viewBox="0 0 12 12"><path d="M2 1h2.5l1 3-1.5 1a6 6 0 0 0 3 3l1-1.5 3 1V10a1 1 0 0 1-1 1A9 9 0 0 1 1 2a1 1 0 0 1 1-1z" fill="#fff"/></svg>
        000-000-0000
      </p>
      <p class="contact-row">
        <svg viewBox="0 0 12 12"><rect x="3" y="1" width="6" height="10" rx="1" fill="none" stroke="#fff" stroke-width="1.3"/></svg>
        000-000-0000
      </p>
      <p class="contact-row">
        <svg viewBox="0 0 12 12"><rect x="1" y="2.5" width="10" height="7" fill="none" stroke="#fff" stroke-width="1.2"/><path d="M1 2.5l5 4 5-4" fill="none" stroke="#fff" stroke-width="1.2"/></svg>
        hello@hearthline.com
      </p>
      <p class="contact-row">
        <svg viewBox="0 0 12 12"><circle cx="6" cy="6" r="5" fill="none" stroke="#fff" stroke-width="1.2"/><path d="M1 6h10M6 1c-2.5 3-2.5 7 0 10M6 1c2.5 3 2.5 7 0 10" fill="none" stroke="#fff" stroke-width="1"/></svg>
        www.hearthline.com
      </p>
    </div>

    <div class="brand">
      <span class="brand-mark"></span>
      <div>
        <div class="brand-name">Hearthline</div>
        <div class="brand-sub">Remodeling Group</div>
      </div>
    </div>
  </section>

</body>
</html>
```